Business Card Design

Business card design.

Business card is to have logo, website address and email address.

Website is www.brightkettle.ie
Email is info@brightkettle.ie

I have ordered Business Card Printing via Print Harbor, the Double-sided colour printed option with gloss finish.

Industry/Entity Type

Business

```html
<!DOCTYPE html>
<html lang="en">
<head>
<meta charset="utf-8">
<title>Bright Kettle – Business Card</title>
<link rel="stylesheet" href="https://fonts.googleapis.com/css2?family=Nunito:wght@600;800&display=swap">
<style>
  :root {
    --page: #ffffff;
    --card: #ffffff;
    --card-edge: #1a1a1a;
    --ink: #111111;
    --accent: #d8120f;
  }
  html, body {
    margin: 0;
    padding: 0;
    overflow: hidden;
  }
  body {
    width: 991px;
    height: 1200px;
    background: var(--page);
    position: relative;
    font-family: "Nunito", sans-serif;
    color: var(--ink);
  }
  .card {
    position: absolute;
    background: var(--card);
    border: 1px solid var(--card-edge);
    box-sizing: border-box;
  }
  .card--front {
    left: 458px;
    top: 170px;
    width: 466px;
    height: 292px;
    display: flex;
    align-items: center;
    justify-content: center;
  }
  .card--back {
    left: 70px;
    top: 640px;
    width: 680px;
    height: 425px;
  }
  .brand {
    display: flex;
    align-items: center;
    gap: 12px;
  }
  .brand__dot {
    width: 34px;
    height: 34px;
    border-radius: 50%;
    background: var(--accent);
    flex: none;
  }
  .brand__name {
    font-weight: 800;
    font-size: 36px;
    letter-spacing: 0.5px;
    color: var(--ink);
    line-height: 1;
    white-space: nowrap;
  }
  .card--back .brand {
    position: absolute;
    left: 40px;
    top: 190px;
    gap: 9px;
  }
  .card--back .brand__dot {
    width: 24px;
    height: 24px;
  }
  .card--back .brand__name {
    font-size: 25px;
  }
  .divider {
    position: absolute;
    left: 322px;
    top: 95px;
    width: 3px;
    height: 245px;
    background: var(--accent);
  }
  .contact {
    position: absolute;
    left: 362px;
    top: 162px;
    margin: 0;
    padding: 0;
    list-style: none;
    font-weight: 600;
    font-size: 21px;
    letter-spacing: 0.3px;
    white-space: nowrap;
  }
  .contact li {
    margin-bottom: 26px;
  }
  .contact__label {
    display: inline-block;
    width: 26px;
  }
</style>
</head>
<body>
  <section class="card card--front" aria-label="Card front">
    <div class="brand">
      <span class="brand__dot"></span>
      <span class="brand__name">BRIGHTKETTLE.IE</span>
    </div>
  </section>

  <section class="card card--back" aria-label="Card back">
    <div class="brand">
      <span class="brand__dot"></span>
      <span class="brand__name">BRIGHTKETTLE.IE</span>
    </div>
    <div class="divider"></div>
    <ul class="contact">
      <li><span class="contact__label">e.</span> info@brightkettle.ie</li>
      <li><span class="contact__label">w.</span> www.brightkettle.ie</li>
    </ul>
  </section>
</body>
</html>
```